IT COMPANYcutting edge tec business card

we are IT company that building any apps.
we need business card in japanese and english
You don’t have to include all information in front one you can attach part of that information to back-side
company name : 株式会社かすみ鳥 (MOSSLARK Inc.)
concept : cutting-edge technology
role : 取締役 (director)
name : 河 泰林 (Ha Taerimmu)
post number : 168-0037
address : 東京都世田谷区北霞台5-08-44 (5-08-44, Kitakasumidai, Setagaya Ku, Tokyo To, 168-0037, Japan)
Tel:+81-3-5917-2843
Mobile:+81-80-7263-5518
Email : taerimha@fieldoflark.com
website : www.fieldoflark.com

we dont have logo so please make it as well
we also looking for designer who can make homapage design.

Designs look the same

Low design quality

Contact Information for Business Card

cutting-edge design and modern for IT

Font styles to use
Sans Serif

Colors
34a6d7
33b8a4
6092c4
3377b5
886aae
6b449b
b868aa
a64599

Requirements
Must have
• Simple but designed

```html
<!DOCTYPE html>
<html lang="ja">
<head>
<meta charset="utf-8">
<title>MOSSLARK Inc. Business Card</title>
<link rel="stylesheet" href="https://fonts.googleapis.com/css2?family=Lato:wght@400;700;900&family=Noto+Sans+JP:wght@400;700&display=swap">
<style>
  :root {
    --navy: #0f2b4d;
    --paper: #ffffff;
    --paper-soft: rgba(255,255,255,.78);
    --backdrop: #3a3a3c;
    --ink: #2b2b2b;
    --logo-grey: #58595b;
    --rule: #9a9a9a;
  }
  * { box-sizing: border-box; margin: 0; padding: 0; }
  html, body { width: 1200px; height: 900px; overflow: hidden; }
  body {
    background: var(--backdrop);
    font-family: "Lato", "Noto Sans JP", sans-serif;
    display: flex;
    flex-direction: column;
    align-items: center;
    justify-content: center;
    gap: 50px;
  }
  .card {
    width: 600px;
    height: 343px;
    border-radius: 18px;
    position: relative;
    box-shadow: 0 10px 24px rgba(0,0,0,.35);
  }
  .card-back {
    background: var(--navy);
    color: var(--paper);
  }
  .wordmark {
    font-family: "Lato", sans-serif;
    font-weight: 700;
    letter-spacing: 0.06em;
    white-space: nowrap;
  }
  .back-brand {
    position: absolute;
    left: 0;
    right: 0;
    top: 132px;
    text-align: center;
  }
  .card-back .wordmark { display: block; font-size: 40px; line-height: 1; }
  .company-ja {
    display: block;
    margin-top: 14px;
    font-family: "Noto Sans JP", sans-serif;
    font-size: 15px;
    font-weight: 400;
    letter-spacing: 0.3em;
    color: var(--paper-soft);
  }
  .back-details {
    position: absolute;
    left: 0;
    right: 0;
    bottom: 30px;
    text-align: center;
    font-family: "Noto Sans JP", sans-serif;
    font-size: 11.5px;
    line-height: 1.7;
    color: var(--paper-soft);
  }
  .back-details .name-ja {
    font-weight: 700;
    color: var(--paper);
    font-size: 13px;
    letter-spacing: 0.1em;
  }
  .card-front { background: var(--paper); }
  .card-front .wordmark {
    position: absolute;
    left: 44px;
    top: 196px;
    color: var(--logo-grey);
    font-size: 28px;
  }
  .divider {
    position: absolute;
    left: 286px;
    top: 84px;
    width: 1px;
    height: 186px;
    background: var(--rule);
  }
  .contact {
    position: absolute;
    left: 318px;
    top: 70px;
    color: var(--ink);
  }
  .person-name {
    font-weight: 900;
    font-size: 27px;
    color: var(--navy);
    line-height: 1.05;
  }
  .person-role { font-size: 13px; margin-top: 2px; }
  .address {
    font-size: 11.5px;
    line-height: 1.35;
    margin-top: 16px;
  }
  .contact-list { list-style: none; margin-top: 10px; }
  .contact-list li {
    display: flex;
    align-items: center;
    gap: 8px;
    font-size: 13px;
    line-height: 1.5;
  }
  .contact-list svg { width: 13px; height: 13px; fill: var(--navy); flex: none; }
</style>
</head>
<body>
  <section class="card card-back">
    <div class="back-brand">
      <span class="wordmark">MOSSLARK INC</span>
      <span class="company-ja">株式会社かすみ鳥</span>
    </div>
    <div class="back-details">
      <p><span class="name-ja">取締役　河 泰林</span></p>
      <p>〒168-0037　東京都世田谷区北霞台5-08-44</p>
    </div>
  </section>

  <section class="card card-front" lang="en">
    <span class="wordmark">MOSSLARK INC</span>
    <div class="divider"></div>
    <div class="contact">
      <h1 class="person-name">Ha Taerimmu</h1>
      <p class="person-role">Director</p>
      <p class="address">5-08-44, Kitakasumidai,<br>Setagaya Ku, Tokyo To, 168-0037, Japan</p>
      <ul class="contact-list">
        <li>
          <svg viewBox="0 0 16 16" aria-hidden="true"><path d="M1 6c0-2 3-3.5 7-3.5S15 4 15 6v1h-3.5V5.5h-7V7H1zM3 8h10l1 6H2zm5 1.6a1.9 1.9 0 1 0 0 3.8 1.9 1.9 0 0 0 0-3.8z"/></svg>
          +81-3-5917-2843
        </li>
        <li>
          <svg viewBox="0 0 16 16" aria-hidden="true"><path d="M4.5 0.5h7a1 1 0 0 1 1 1v13a1 1 0 0 1-1 1h-7a1 1 0 0 1-1-1v-13a1 1 0 0 1 1-1zm.5 2v9.5h6V2.5zm3 10.3a.9.9 0 1 0 0 1.8.9.9 0 0 0 0-1.8z"/></svg>
          +81-80-7263-5518
        </li>
        <li>
          <svg viewBox="0 0 16 16" aria-hidden="true"><path d="M1 3h14v.8L8 9 1 3.8zm0 2.2 7 5.2 7-5.2V13H1z"/></svg>
          taerimha@fieldoflark.com
        </li>
        <li>
          <svg viewBox="0 0 16 16" aria-hidden="true"><path d="M8 1a7 7 0 1 0 0 14A7 7 0 0 0 8 1zm0 1.3c.9.8 1.6 2.3 1.9 4H6.1C6.4 4.6 7.1 3.1 8 2.3zM2.4 7.3h2.4c0 .5 0 1 .1 1.4H2.4a5.7 5.7 0 0 1 0-1.4zm3.7 0h3.8a10 10 0 0 1 0 1.4H6.1a10 10 0 0 1 0-1.4zm5 0h2.5a5.7 5.7 0 0 1 0 1.4h-2.5c.1-.4.1-.9 0-1.4zM6.1 9.9h3.8c-.3 1.7-1 3.1-1.9 3.9-.9-.8-1.6-2.2-1.9-3.9z"/></svg>
          www.fieldoflark.com
        </li>
      </ul>
    </div>
  </section>
</body>
</html>
```